Stationery and business card design
TradeNimbus
Stationery and business card design -
Creative Brief
Corporate
Marcella Quenby, PHR, PMP
Project Manager
4172 Birchwell Rd NE #20591 Oakhollow, MI 48273
mquenby@tradenimbus.example
http://www.tradenimbus.example
stationary will be for corporate entity no specific individual

```html
<!DOCTYPE html>
<html lang="en">
<head>
<meta charset="utf-8">
<title>TradeNimbus Stationery</title>
<link href="https://fonts.googleapis.com/css2?family=Open+Sans:wght@400;600&display=swap" rel="stylesheet">
<style>
  :root {
    --bg: #e6e3de;
    --paper: #ffffff;
    --paper-edge: #e2e2e2;
    --brand-blue: #2f6fb8;
    --brand-orange: #f39a1e;
    --ink: #3b4f6e;
    --ink-soft: #6b7789;
  }
  * { margin: 0; padding: 0; box-sizing: border-box; }
  html, body { width: 1200px; height: 866px; overflow: hidden; }
  body {
    background: var(--bg);
    font-family: "Open Sans", Arial, sans-serif;
    position: relative;
  }
  .sheet {
    position: absolute;
    background: var(--paper);
    box-shadow: 0 2px 8px rgba(0,0,0,0.18);
    overflow: hidden;
  }
  .swoosh { position: absolute; left: 0; bottom: 0; width: 100%; display: block; }
  .brand-name {
    position: absolute;
    color: var(--ink);
    font-weight: 600;
    letter-spacing: -0.5px;
    white-space: nowrap;
  }
  .contact {
    position: absolute;
    text-align: right;
    color: var(--ink-soft);
    line-height: 1.45;
  }
  .contact .label { color: var(--brand-orange); }
  .contact .web { color: var(--brand-orange); }

  /* Letterhead */
  .letterhead { left: 48px; top: 108px; width: 516px; height: 665px; }
  .letterhead .brand-name { left: 40px; top: 40px; font-size: 30px; }
  .letterhead .contact { right: 36px; top: 40px; font-size: 8px; }
  .letterhead .swoosh { height: 80px; }

  /* Business card */
  .business-card { left: 696px; top: 360px; width: 164px; height: 96px; }
  .business-card .brand-name { left: 12px; top: 14px; font-size: 15px; }
  .business-card .card-person {
    position: absolute; left: 12px; top: 50px;
    font-size: 5px; color: var(--ink); line-height: 1.4;
  }
  .business-card .contact { right: 10px; top: 44px; font-size: 4.2px; }
  .business-card .swoosh { height: 22px; }

  /* Envelope back */
  .envelope-back { left: 523px; top: 450px; width: 605px; height: 124px; }
  .envelope-back .flap { position: absolute; left: 0; top: 0; width: 100%; height: 100%; display: block; }
  .envelope-back .flap-name {
    position: absolute; left: 0; width: 100%; top: 22px;
    text-align: center; color: var(--paper); font-size: 14px; font-weight: 600;
  }

  /* Envelope front */
  .envelope-front { left: 588px; top: 500px; width: 594px; height: 168px; }
  .envelope-front .brand-name { left: 28px; top: 26px; font-size: 26px; }
  .envelope-front .contact { right: 28px; top: 28px; font-size: 7.5px; }
  .envelope-front .swoosh { height: 50px; }
</style>
</head>
<body>

<section class="sheet letterhead">
  <div class="brand-name">TradeNimbus</div>
  <div class="contact">
    4172 Birchwell Rd NE #20591<br>
    Oakhollow, MI 48273<br>
    <span class="label">Toll Free:</span> 1.800.555.0142<br>
    <span class="label">E-mail:</span> mquenby@tradenimbus.example<br>
    <span class="web">http://www.tradenimbus.example</span>
  </div>
  <svg class="swoosh" viewBox="0 0 500 80" preserveAspectRatio="none" aria-hidden="true">
    <path d="M0 42 Q250 -8 500 20 L500 80 L0 80 Z" fill="var(--brand-orange)"/>
    <path d="M0 50 Q250 4 500 28 L500 80 L0 80 Z" fill="var(--paper)"/>
    <path d="M0 56 Q250 14 500 34 L500 80 L0 80 Z" fill="var(--brand-blue)"/>
  </svg>
</section>

<section class="sheet envelope-back">
  <svg class="flap" viewBox="0 0 605 124" preserveAspectRatio="none" aria-hidden="true">
    <path d="M0 0 L605 0 L605 14 Q330 40 302 70 Q275 40 0 14 Z" fill="var(--brand-blue)"/>
  </svg>
  <div class="flap-name">TradeNimbus</div>
</section>

<section class="sheet envelope-front">
  <div class="brand-name">TradeNimbus</div>
  <div class="contact">
    4172 Birchwell Rd NE #20591<br>
    Oakhollow, MI 48273<br>
    <span class="label">Toll Free:</span> 1.800.555.0142<br>
    <span class="label">E-mail:</span> mquenby@tradenimbus.example<br>
    <span class="web">http://www.tradenimbus.example</span>
  </div>
  <svg class="swoosh" viewBox="0 0 600 50" preserveAspectRatio="none" aria-hidden="true">
    <path d="M0 24 Q300 -10 600 8 L600 50 L0 50 Z" fill="var(--brand-orange)"/>
    <path d="M0 30 Q300 0 600 14 L600 50 L0 50 Z" fill="var(--paper)"/>
    <path d="M0 34 Q300 8 600 19 L600 50 L0 50 Z" fill="var(--brand-blue)"/>
  </svg>
</section>

<section class="sheet business-card">
  <div class="brand-name">TradeNimbus</div>
  <div class="card-person">
    Marcella Quenby, PHR, PMP<br>
    Project Manager
  </div>
  <div class="contact">
    4172 Birchwell Rd NE #20591<br>
    Oakhollow, MI 48273<br>
    mquenby@tradenimbus.example<br>
    http://www.tradenimbus.example
  </div>
  <svg class="swoosh" viewBox="0 0 164 22" preserveAspectRatio="none" aria-hidden="true">
    <path d="M0 11 Q82 -3 164 4 L164 22 L0 22 Z" fill="var(--brand-orange)"/>
    <path d="M0 14 Q82 1 164 7 L164 22 L0 22 Z" fill="var(--paper)"/>
    <path d="M0 16 Q82 4 164 9 L164 22 L0 22 Z" fill="var(--brand-blue)"/>
  </svg>
</section>

</body>
</html>
```